Creative design for PLW Businesscard!

We would like a creative business card for our company The Maple Workshop. We situated in Barcelona and setup software development teams for companies in Belgium, Holland.

Orange is related to Holland.
PLW means cool in Dutch

* An Overview / Background of the Business & Services
o Setup and manage developer teams in Barcelona for for companies
in Holland, Belgium.
* The Target Market / Audience you are trying to reach
o Companies in Holland searching for developers
* Design Specifics; any preferences or ideas for Style, Colour,
Imagery, etc
o Orange, professional, fancy
o The Maple Workshop (PLW) means cool , good, nice

Target Market(s)

Companies in Holland searching for developers

Industry/Entity Type

Business

Contact Information for Business Card

Company name: The Maple Workshop

Name: Joost ter Haarveld

Title: Managing director (not necessary)

Email: joost@themapleworkshop.es

web: www.themapleworkshop.es

Phone: (+34) 932 487 113

Mobile: (+34) 668 302 947

Font styles to use
Other font styles liked:
• Bookman Old Style or Rockwell

Requirements
Must have
• Setup and manage developer teams in Barcelona for for companies
• in Holland, Belgium.

```html
<!DOCTYPE html>
<html lang="en">
<head>
<meta charset="utf-8">
<title>The Maple Workshop – Business Card</title>
<link rel="stylesheet" href="https://fonts.googleapis.com/css2?family=Arvo:wght@400;700&family=Arimo:wght@400;700&display=swap">
<style>
  :root {
    --orange: #ef7236;
    --orange-line: #e0662c;
    --ink: #3d3d3d;
    --text: #333333;
    --paper: #ffffff;
    --backdrop: #e9e9e9;
  }
  html, body {
    margin: 0;
    padding: 0;
    width: 1010px;
    height: 1200px;
    overflow: hidden;
    background: var(--backdrop);
  }
  .card {
    position: absolute;
    left: 125px;
    top: 495px;
    width: 759px;
    height: 210px;
    background: var(--paper);
    box-shadow: 0 1px 4px rgba(0,0,0,0.15);
  }
  .card__front {
    position: absolute;
    left: 0; top: 0;
    width: 380px; height: 210px;
    background: var(--orange);
  }
  .logo-box {
    position: absolute;
    left: 38px; top: 38px;
    width: 300px; height: 131px;
    background: var(--paper);
    border: 2px solid var(--orange-line);
    display: flex;
    align-items: center;
    justify-content: center;
  }
  .logo-box__name {
    font-family: "Arimo", Arial, sans-serif;
    font-weight: 700;
    font-size: 56px;
    line-height: 1;
    color: var(--ink);
  }
  .name-bar {
    position: absolute;
    left: 380px; top: 38px;
    width: 159px; height: 17px;
    background: var(--orange);
    color: var(--paper);
    font-family: "Arimo", Arial, sans-serif;
    font-weight: 700;
    font-size: 9px;
    line-height: 17px;
    text-transform: uppercase;
    padding-left: 40px;
    box-sizing: border-box;
    white-space: nowrap;
  }
  .job-title {
    position: absolute;
    left: 420px; top: 61px;
    font-family: "Arimo", Arial, sans-serif;
    font-size: 9px;
    color: var(--orange);
  }
  .contacts {
    position: absolute;
    left: 410px; top: 101px;
    margin: 0; padding: 0;
    list-style: none;
    font-family: "Arimo", Arial, sans-serif;
    font-size: 9.5px;
    color: var(--text);
  }
  .contacts li {
    display: flex;
    align-items: center;
    height: 19.5px;
  }
  .contacts svg {
    width: 8px; height: 8px;
    margin-right: 4px;
    flex: none;
  }
  .company-name {
    position: absolute;
    left: 601px; top: 33px;
    margin: 0;
    font-family: "Arvo", "Rockwell", serif;
    font-weight: 400;
    font-size: 20.5px;
    line-height: 21px;
    color: var(--orange);
    text-transform: uppercase;
    white-space: nowrap;
  }
</style>
</head>
<body>
  <div class="card">
    <div class="card__front">
      <div class="logo-box">
        <span class="logo-box__name">PLW</span>
      </div>
    </div>

    <div class="name-bar">Joost ter Haarveld</div>
    <div class="job-title">Managing director</div>

    <ul class="contacts">
      <li>
        <svg viewBox="0 0 8 8"><circle cx="4" cy="4" r="4" fill="#ef7236"/><rect x="2" y="2.8" width="4" height="2.6" fill="none" stroke="#fff" stroke-width="0.7"/></svg>
        joost@themapleworkshop.es
      </li>
      <li>
        <svg viewBox="0 0 8 8"><circle cx="4" cy="4" r="4" fill="#ef7236"/><circle cx="4" cy="4" r="2" fill="none" stroke="#fff" stroke-width="0.6"/><line x1="2" y1="4" x2="6" y2="4" stroke="#fff" stroke-width="0.5"/></svg>
        www.themapleworkshop.es
      </li>
      <li>
        <svg viewBox="0 0 8 8"><circle cx="4" cy="4" r="4" fill="#ef7236"/><path d="M2.6 2.2 L3.6 3.4 L3.1 4 Q3.8 5 4.4 5.2 L5 4.6 L6 5.6 L5.4 6.1 Q3.5 5.9 2.2 3 Z" fill="#fff"/></svg>
        (+34) 932 487 113
      </li>
      <li>
        <svg viewBox="0 0 8 8"><circle cx="4" cy="4" r="4" fill="#ef7236"/><rect x="2.9" y="1.8" width="2.2" height="4.4" rx="0.4" fill="none" stroke="#fff" stroke-width="0.6"/></svg>
        (+34) 668 302 947
      </li>
    </ul>

    <h1 class="company-name">The<br>Maple<br>Workshop</h1>
  </div>
</body>
</html>
```